Outdoor kitchen and Appliance Need new business card

We need a new business card, for our business.

Front side with all info, back side with more brand identity.

I have attached some drafts, we moved up but it lacks creativity.

Use https://photos.quendrix.com and I can purchase, the stock photo and send it you if you design is chosen.

We are also planing on printing business card with the logo, having a spot uv. I have attached instructions.

Plumtarvessa.com is our website

Target Market(s)

Extremely high end customer.

Contact Information for Business Card

Double sided with spot uv on logos

Colors
ec1f27

Requirements
Must have
• See sample I have attached, we are open to ideas.

Colors, are: RED, Stainless steel, Black

```html
<!DOCTYPE html>
<html lang="en">
<head>
<meta charset="utf-8">
<title>Plumtarvessa Business Card</title>
<link href="https://fonts.googleapis.com/css2?family=Montserrat:wght@400;500;600&display=swap" rel="stylesheet">
<style>
  :root {
    --bg: #b1b1ac;
    --card: #1d1d1e;
    --card-edge: #e03a40;
    --red: #ec1f27;
    --white: #f2f2f2;
    --gloss: #4a4a4c;
    --gloss-light: #5c5c5f;
  }
  * { margin: 0; padding: 0; box-sizing: border-box; }
  html, body { width: 1200px; height: 801px; overflow: hidden; }
  body {
    background: var(--bg);
    font-family: "Montserrat", sans-serif;
    display: flex;
    align-items: center;
    justify-content: center;
    gap: 40px;
  }
  .card {
    position: relative;
    width: 520px;
    height: 297px;
    background: var(--card);
    border-bottom: 4px solid var(--card-edge);
    box-shadow: 0 14px 28px rgba(0,0,0,0.28);
  }
  .brand {
    display: flex;
    align-items: center;
    gap: 10px;
    color: var(--gloss-light);
    font-weight: 600;
    letter-spacing: 0.5px;
  }
  .brand-dot {
    border-radius: 50%;
    background: var(--gloss);
    flex: none;
  }
  /* front */
  .card-front .brand {
    position: absolute;
    left: 28px;
    top: 132px;
    font-size: 24px;
  }
  .card-front .brand-dot { width: 18px; height: 18px; }
  .divider {
    position: absolute;
    left: 236px;
    top: 40px;
    width: 1px;
    height: 217px;
    background: var(--red);
  }
  .contact {
    position: absolute;
    left: 256px;
    top: 38px;
    color: var(--white);
    font-size: 11.5px;
    line-height: 1.45;
  }
  .contact-name {
    color: var(--red);
    font-size: 19px;
    font-weight: 500;
    text-transform: uppercase;
    line-height: 1.1;
  }
  .contact-title { margin-bottom: 6px; }
  .contact-office {
    color: var(--red);
    font-weight: 500;
    text-transform: uppercase;
  }
  .contact-address { margin-bottom: 6px; }
  .contact-list { list-style: none; }
  .contact-list li { display: flex; align-items: center; gap: 8px; }
  .contact-list svg { width: 10px; height: 10px; flex: none; }
  .contact-list strong { font-weight: 600; }
  /* back */
  .card-back .brand {
    position: absolute;
    inset: 0;
    justify-content: center;
    font-size: 34px;
  }
  .card-back .brand-dot { width: 24px; height: 24px; }
</style>
</head>
<body>
  <section class="card card-front" aria-label="Business card front">
    <div class="brand"><span class="brand-dot"></span>Plumtarvessa</div>
    <div class="divider"></div>
    <div class="contact">
      <p class="contact-name">Dorian Vasquel</p>
      <p class="contact-title">Sales Manager</p>
      <p class="contact-office">Office - Showroom</p>
      <p class="contact-address">480 N Calloway Ct Suite 4<br>Westhaven, FL 30912</p>
      <ul class="contact-list">
        <li><svg viewBox="0 0 10 10"><rect x="2.5" y="0.5" width="5" height="9" rx="1" fill="none" stroke="var(--red)"/></svg>(555)201-4433 <strong>(Cell)</strong></li>
        <li><svg viewBox="0 0 10 10"><path d="M2 1 L4 1 L4.5 3 L3.3 4 Q4.5 6 6 6.7 L7 5.5 L9 6 L9 8 Q5 9 2.5 6 Q1 4 2 1Z" fill="var(--red)"/></svg>(555)318-2260 Office</li>
        <li><svg viewBox="0 0 10 10"><rect x="1" y="4" width="8" height="5" fill="var(--red)"/><rect x="3" y="1" width="4" height="3" fill="none" stroke="var(--red)"/></svg>(555)318-2261</li>
        <li><svg viewBox="0 0 10 10"><rect x="0.5" y="2" width="9" height="6" fill="none" stroke="var(--red)"/><path d="M0.5 2 L5 5.5 L9.5 2" fill="none" stroke="var(--red)"/></svg>Dorian@Plumtarvessa.com</li>
        <li><svg viewBox="0 0 10 10"><circle cx="5" cy="5" r="4.3" fill="none" stroke="var(--red)"/><ellipse cx="5" cy="5" rx="1.8" ry="4.3" fill="none" stroke="var(--red)"/><path d="M0.7 5 H9.3" stroke="var(--red)"/></svg>www.Plumtarvessa.com</li>
      </ul>
    </div>
  </section>

  <section class="card card-back" aria-label="Business card back">
    <div class="brand"><span class="brand-dot"></span>Plumtarvessa</div>
  </section>
</body>
</html>
```